ZEPRILO.COM is a premium domain sales company. Our competitors are companies like vastplots.example, getparcels.example, peerwords.example. Our current site is at www.zeprilos.example.

We want to have the ability to search for domains, to highlight special offers and have some testimonials on the index page.

The logo for the site is attached.

Please be sure that the order form fits on the screen without scrolling the page. I want the entire form, including the submit button to fit without any page scrolling.

Delivered product - INDEX PAGE, ORDER FORM AND CONTENT PAGE PSDs.

Target Market(s)

Small to Medium business professionals

Industry/Entity Type

It Company

Requirements
Must have
• 1. List of domains for sale
2. Simple search box with button to run the search
3. link for advanced search
4. testimonial area. Note - this can be a small box where a different testimonial is displayed on each page load.
Nice to have
• Would like the site to have some white space. Don't want a heavily packed website. Give it an "airy" feel.

```html
<!DOCTYPE html>
<html lang="en">
<head>
<meta charset="utf-8">
<title>ZEPRILO.COM – Domains for Sale</title>
<link href="https://fonts.googleapis.com/css2?family=Open+Sans:ital,wght@0,300;0,400;0,600;0,700;0,800;1,400;1,600&display=swap" rel="stylesheet">
<style>
  :root{
    --page:#f9f9f9;
    --panel:#fafafa;
    --green:#3a9a48;
    --green-soft:#6ab27a;
    --navy:#0d4e95;
    --yellow:#fec43f;
    --orange:#e07a2e;
    --text:#6f6f6f;
    --text-light:#8a8a8a;
    --muted:#aaaaaa;
    --band-a:#78ace2;
    --band-b:#a8cdf1;
    --ribbon:#e84a4c;
  }
  *{box-sizing:border-box;margin:0;padding:0}
  html,body{width:1108px;height:1200px;overflow:hidden}
  body{background:var(--page);font-family:"Open Sans",Arial,sans-serif;position:relative;color:var(--text)}

  .testimonials{position:absolute;left:51px;top:90px;width:208px}
  .testimonials h2{font-size:22px;font-weight:700;color:var(--green-soft);line-height:1.1}
  .testimonials .sub{font-size:16px;font-style:italic;color:var(--green-soft);margin-top:2px}
  .testimonials blockquote{font-size:11.5px;color:#333;text-align:right;line-height:22px;margin-top:2px}
  .testimonials cite{font-style:normal;font-weight:700}

  .brand{position:absolute;left:346px;top:62px;width:240px;display:flex;align-items:center;gap:8px}
  .brand-name{font-size:30px;font-weight:800;color:var(--navy);letter-spacing:-0.5px;white-space:nowrap;line-height:40px}
  .brand-mark{flex:none;width:10px;height:10px;border-radius:50%;background:var(--green)}
  .tagline{position:absolute;left:596px;top:68px;font-size:16.5px;font-weight:700;color:var(--yellow);line-height:26px;white-space:nowrap}

  .search{position:absolute;left:346px;top:135px;width:416px}
  .search label{font-size:16px;color:var(--muted)}
  .search-box{margin-top:2px;height:44px;border-radius:4px;background:linear-gradient(112deg,#e6e6e6 0 62%,#f0f0f0 62% 72%,#ececec 72%);display:flex;align-items:center;justify-content:space-between;padding:0 12px}
  .search-box .query{font-size:25px;font-weight:600;color:#444;border-right:1.5px solid #444;padding-right:1px;line-height:30px}
  .search-box .go{font-size:24px;font-weight:800;color:var(--green)}
  .advanced{position:absolute;right:346px;top:206px;font-size:17.5px;color:var(--navy);text-decoration:none}

  .offers{position:absolute;left:847px;top:93px}
  .offers h2{font-size:20px;font-weight:600;color:var(--green-soft);margin-bottom:2px}
  .offers li{list-style:none;font-size:16.5px;font-weight:600;color:var(--muted);line-height:26px}
  .offers small{font-size:12px;font-weight:400}

  .panel{position:absolute;left:114px;top:295px;width:879px;height:920px;background:var(--panel);box-shadow:0 0 18px rgba(0,0,0,.08)}
  .panel-title{position:absolute;left:53px;top:6px;font-size:36px;font-weight:400;color:var(--green);letter-spacing:.5px}
  .nav{position:absolute;left:596px;top:18px;display:flex;gap:22px;font-size:14px}
  .nav a{text-decoration:none;color:var(--navy);display:flex;align-items:center;gap:6px}
  .nav a.active{color:var(--yellow)}

  .band{position:absolute;left:0;top:350px;width:1108px;height:50px;background:linear-gradient(180deg,var(--band-a),var(--band-b))}
  .band .col{position:absolute;top:10px;font-size:22px;color:#fff;letter-spacing:.5px}
  .pager{position:absolute;left:827px;top:24px;display:flex;gap:14px;align-items:center;font-size:12px;color:#fff;line-height:14px}
  .pager span{font-size:12px}

  .domains{position:absolute;left:0;top:420px;width:1108px}
  .row{height:46.15px;position:relative;display:flex;align-items:center}
  .row .name{position:absolute;left:172px;font-size:18px;color:var(--text)}
  .row .name small{font-size:17px;color:var(--text-light)}
  .row .cat{position:absolute;left:485px;font-size:17px;color:var(--text-light)}
  .row .price{position:absolute;left:697px;font-size:17px;color:var(--text-light)}
  .buy{position:absolute;left:844px;width:91px;height:37px;border-radius:13px;background:var(--yellow);color:#fff;font-size:16.5px;display:flex;align-items:center;justify-content:center;text-decoration:none}
  .buy.hover{background:var(--orange)}
  .ribbon{position:absolute;left:54px;top:-26px;width:112px;height:62px}
</style>
</head>
<body>

<section class="testimonials">
  <h2>Testimonials</h2>
  <p class="sub">What people think about us</p>
  <blockquote>"Fast and smooth transaction.<br>Thanks" – <cite>Marek</cite></blockquote>
</section>

<div class="brand"><span class="brand-name">ZEPRILO.COM</span><span class="brand-mark"></span></div>
<p class="tagline">Buy your internet<br>Domains</p>

<form class="search">
  <label>Search domain name</label>
  <div class="search-box"><span class="query">cars-classic.com</span><span class="go">GO</span></div>
</form>
<a class="advanced" href="#">+ Advanced Search</a>

<aside class="offers">
  <h2>Special Premium Offers</h2>
  <ul>
    <li>coastwallets<small>.com only $100</small></li>
    <li>gamerkonsolen<small>.com only $200</small></li>
    <li>believe1<small>.com only $180</small></li>
  </ul>
</aside>

<main class="panel">
  <h1 class="panel-title">DOMAINS FOR SALE</h1>
  <nav class="nav">
    <a href="#">HOME <svg width="16" height="15" viewBox="0 0 16 15"><path d="M8 1 1 8h2v6h4v-4h2v4h4V8h2z" fill="#8fb8e6"/></svg></a>
    <a href="#" class="active">ABOUT <svg width="20" height="18" viewBox="0 0 20 18"><g fill="none" stroke="#8fb8e6" stroke-width="2.4"><rect x="2" y="7" width="9" height="6" rx="3" transform="rotate(-40 6 10)"/><rect x="8" y="4" width="9" height="6" rx="3" transform="rotate(-40 12 7)"/></g></svg></a>
    <a href="#">FAQ <svg width="18" height="18" viewBox="0 0 18 18"><circle cx="9" cy="9" r="8.5" fill="#8fb8e6"/><text x="9" y="13.5" text-anchor="middle" font-size="12" font-weight="700" fill="#fff" font-family="Open Sans,sans-serif">?</text></svg></a>
  </nav>
</main>

<div class="band">
  <span class="col" style="left:171px">Domain</span>
  <span class="col" style="left:485px">Category</span>
  <span class="col" style="left:697px">Price</span>
  <div class="pager"><span>◂ PREVIOUS</span><span>NEXT ▸</span></div>
</div>

<svg width="0" height="0" style="position:absolute">
  <defs>
    <g id="offer-tag">
      <g transform="rotate(22 56 31)">
        <polygon points="4,16 92,16 108,31 92,46 4,46" fill="var(--ribbon)"/>
        <text x="50" y="36" text-anchor="middle" font-family="Open Sans,sans-serif" font-size="12.5" font-weight="700" font-style="italic" fill="#fff">Special Offer!</text>
      </g>
    </g>
  </defs>
</svg>

<section class="domains">
  <div class="row"><span class="name">Aczclovir<small>.com</small></span><span class="cat">Health</span><span class="price">$100.00</span><a class="buy" href="#">Buy Now</a></div>
  <div class="row"><svg class="ribbon" viewBox="0 0 112 62"><use href="#offer-tag"/></svg><span class="name">coastwallets<small>.com</small></span><span class="cat">Sports</span><span class="price">$100.00</span><a class="buy hover" href="#">Buy Now</a></div>
  <div class="row"><span class="name">cars-classic<small>.com</small></span><span class="cat">Vehicles</span><span class="price">$4397.00</span><a class="buy" href="#">Buy Now</a></div>
  <div class="row"><span class="name">newhorizauto<small>.com</small></span><span class="cat">Vehicles</span><span class="price">$999.00</span><a class="buy" href="#">Buy Now</a></div>
  <div class="row"><svg class="ribbon" viewBox="0 0 112 62"><use href="#offer-tag"/></svg><span class="name">descacrcamuyica<small>.com</small></span><span class="cat">Other</span><span class="price">$197.00</span><a class="buy" href="#">Buy Now</a></div>
  <div class="row"><span class="name">allthehouses<small>.com</small></span><span class="cat">Real Estate</span><span class="price">$100.00</span><a class="buy" href="#">Buy Now</a></div>
  <div class="row"><span class="name">news-a<small>.com</small></span><span class="cat">Media</span><span class="price">$300.00</span><a class="buy" href="#">Buy Now</a></div>
  <div class="row"><span class="name">procesosindustriales<small>.com</small></span><span class="cat">Law</span><span class="price">$211.00</span><a class="buy" href="#">Buy Now</a></div>
  <div class="row"><span class="name">cleardebtsolutions<small>.com</small></span><span class="cat">Finance</span><span class="price">$999.00</span><a class="buy" href="#">Buy Now</a></div>
  <div class="row"><span class="name">ohzah<small>.com</small></span><span class="cat">Other</span><span class="price">$100.00</span><a class="buy" href="#">Buy Now</a></div>
  <div class="row"><span class="name">siye14<small>.net</small></span><span class="cat">Other</span><span class="price">$129.00</span><a class="buy" href="#">Buy Now</a></div>
  <div class="row"><span class="name">rechargeworld<small>.com</small></span><span class="cat">Society</span><span class="price">$999.00</span><a class="buy" href="#">Buy Now</a></div>
  <div class="row"><span class="name">gamekonsolen<small>.com</small></span><span class="cat">Food</span><span class="price">$999.00</span><a class="buy" href="#">Buy Now</a></div>
  <div class="row"><svg class="ribbon" viewBox="0 0 112 62"><use href="#offer-tag"/></svg><span class="name">sanjosehomesforsale<small>.net</small></span><span class="cat">Real Estate</span><span class="price">$397.00</span><a class="buy" href="#">Buy Now</a></div>
  <div class="row"><span class="name">believe1<small>.com</small></span><span class="cat">Other</span><span class="price">$97.00</span><a class="buy" href="#">Buy Now</a></div>
  <div class="row"><span class="name">pizzapalvouchers<small>.com</small></span><span class="cat">Food</span><span class="price">$100.00</span><a class="buy" href="#">Buy Now</a></div>
  <div class="row"><span class="name">phil/cordell<small>.com</small></span><span class="cat">Other</span><span class="price">$700.00</span><a class="buy" href="#">Buy Now</a></div>
</section>

</body>
</html>
```